Kelvo Tech Oz Business card revamp

We are looking to revamp our business card design. We are hoping to change our colours to dark navey blue, gray, white and black but are open to keeping the same if a good design is submited. We are after somthing a bit differnt not just boring business card. I have attached a copy of our current card. We Want to keep the same logo design which i have attached a few to hopfully help you in this process. We are after a design that can be personalized to separate 4 people

Colors
0455a3
ffffff
000000
cbcbcb

Requirements
Must have
• Kelvo Tech Logo, address 3/41 Mallory Court, Wexhill 4218, phone number, Name and position

```html
<!DOCTYPE html>
<html lang="en">
<head>
<meta charset="utf-8">
<title>Kelvo Tech Oz — Business Card</title>
<link rel="stylesheet" href="https://fonts.googleapis.com/css2?family=Lato:wght@400;700;900&display=swap">
<style>
  :root {
    --stage: #e4e4e4;
    --card: #232629;
    --card-edge: #1a1c1e;
    --brand-blue: #2f86d6;
    --brand-orange: #f47a20;
    --text-light: #f2f2f2;
  }
  * { margin: 0; padding: 0; box-sizing: border-box; }
  html, body { width: 1200px; height: 780px; overflow: hidden; }
  body {
    background: var(--stage);
    font-family: "Lato", sans-serif;
    position: relative;
  }
  .card {
    position: absolute;
    width: 525px;
    height: 300px;
    border-radius: 22px;
    background: var(--card);
    overflow: hidden;
    box-shadow: 0 3px 0 var(--card-edge), 0 14px 30px rgba(0,0,0,0.25);
  }
  .card-front { left: 70px; top: 80px; }
  .card-back { left: 605px; top: 400px; }

  .front-texture {
    position: absolute; inset: 0;
    background: radial-gradient(ellipse at 50% 45%, #2a2d31 0%, #212427 70%);
  }
  .brand {
    display: flex; align-items: center; gap: 10px;
    font-weight: 900; color: var(--brand-blue);
    letter-spacing: 0.5px; white-space: nowrap;
  }
  .brand-dot {
    border-radius: 50%; background: var(--brand-orange); flex: none;
  }
  .card-front .brand {
    position: absolute; left: 50%; top: 50%;
    transform: translate(-50%, -50%);
    font-size: 46px;
  }
  .card-front .brand-dot { width: 40px; height: 40px; }

  .card-back .brand {
    position: absolute; left: 34px; top: 114px;
    font-size: 30px;
  }
  .card-back .brand-dot { width: 26px; height: 26px; }

  .divider {
    position: absolute; left: 300px; top: 74px;
    width: 2px; height: 140px; background: var(--brand-orange);
  }
  .contact {
    position: absolute; left: 326px; top: 66px;
    color: var(--text-light);
  }
  .person-name { font-size: 22px; font-weight: 700; line-height: 1.05; }
  .person-name .first { color: var(--brand-blue); }
  .person-name .last { color: var(--brand-orange); }
  .person-role { font-size: 15px; margin-bottom: 16px; }
  .contact-line {
    display: flex; align-items: center; gap: 8px;
    font-size: 14px; line-height: 1.5;
  }
  .contact-line svg { flex: none; }
  .address { font-size: 14px; line-height: 1.35; margin-top: 4px; }

  .colour-band {
    position: absolute; left: 0; right: 0; bottom: 0; height: 18px;
    display: flex;
  }
  .band-blue { width: 44%; background: var(--brand-blue); }
  .band-orange { flex: 1; background: var(--brand-orange); }
</style>
</head>
<body>
  <section class="card card-front" aria-label="Card front">
    <div class="front-texture" role="img" aria-label="Faint tonal background texture"></div>
    <div class="brand"><span class="brand-dot"></span>Kelvo Tech</div>
  </section>

  <section class="card card-back" aria-label="Card back">
    <div class="brand"><span class="brand-dot"></span>Kelvo Tech</div>
    <div class="divider"></div>
    <div class="contact">
      <p class="person-name"><span class="first">Dana</span> <span class="last">Hollis</span></p>
      <p class="person-role">Manager</p>
      <p class="contact-line">
        <svg width="16" height="16" viewBox="0 0 16 16" aria-hidden="true">
          <circle cx="8" cy="8" r="7.2" fill="none" stroke="var(--brand-orange)" stroke-width="1.4"/>
          <path d="M5.4 4.4l1.3-.3.8 1.8-.9.7c.4.9 1.1 1.6 2 2l.7-.9 1.8.8-.3 1.3c-2.8.2-5.6-2.6-5.4-5.4z" fill="var(--brand-orange)"/>
        </svg>
        07 4410 2639
      </p>
      <p class="contact-line">
        <svg width="16" height="16" viewBox="0 0 16 16" aria-hidden="true">
          <circle cx="8" cy="8" r="7.2" fill="none" stroke="var(--brand-orange)" stroke-width="1.4"/>
          <circle cx="8" cy="8" r="4" fill="none" stroke="var(--brand-orange)" stroke-width="1"/>
          <path d="M4 8h8M8 4c-1.5 2.5-1.5 5.5 0 8M8 4c1.5 2.5 1.5 5.5 0 8" fill="none" stroke="var(--brand-orange)" stroke-width="1"/>
        </svg>
        www.kelvotech.com.au
      </p>
      <p class="address">3/41 Mallory Court<br>Wexhill, Qld 4218</p>
    </div>
    <div class="colour-band"><span class="band-blue"></span><span class="band-orange"></span></div>
  </section>
</body>
</html>
```